Rogue Zinfandel wine label

I need a wine label designed for a new wine brand. I am open to anything, but I think the simpler and bolder the better so it will stand out on the shelf amongst the hundreds of brands out there.
Label should have the word ROGUE buy itself with the word Zinfandel under it.

```html
<!DOCTYPE html>
<html lang="en">
<head>
<meta charset="utf-8">
<title>Rogue Zinfandel – Wine Label</title>
<link rel="stylesheet" href="https://fonts.googleapis.com/css2?family=Cinzel:wght@400&family=Didact+Gothic&family=Pinyon+Script&family=UnifrakturMaguntia&display=swap">
<style>
  :root {
    --paper: #ffffff;
    --gold: #f6c25c;
    --shade: #bbbbbb;
    --ink: #000000;
    --gold-deep: #b8893a;
  }
  html, body {
    margin: 0;
    padding: 0;
    overflow: hidden;
    background: var(--paper);
  }
  .label {
    position: relative;
    width: 1005px;
    height: 1200px;
    overflow: hidden;
    background: var(--paper);
  }
  .shade {
    position: absolute;
    left: 0;
    top: 0;
    width: 1005px;
    height: 1200px;
  }
  .stripes {
    position: absolute;
    left: 0;
    top: 0;
    width: 970px;
    height: 1200px;
    background: repeating-linear-gradient(
      to right,
      transparent 0px,
      transparent 30px,
      var(--gold) 30px,
      var(--gold) 43px
    );
    background-size: 42px 100%;
    mix-blend-mode: multiply;
  }
  .glass {
    position: absolute;
    left: 396px;
    top: 204px;
    width: 227px;
    height: 451px;
  }
  .vintage,
  .brand,
  .varietal,
  .spec {
    position: absolute;
    margin: 0;
    padding: 0;
    white-space: nowrap;
  }
  .vintage,
  .brand,
  .varietal {
    left: 0;
    width: 100%;
    text-align: center;
  }
  .vintage {
    top: 676px;
    font-family: "UnifrakturMaguntia", serif;
    font-weight: 400;
    font-size: 100px;
    line-height: 1;
    color: var(--ink);
  }
  .brand {
    top: 790px;
    font-family: "Cinzel", serif;
    font-weight: 400;
    font-size: 176px;
    line-height: 1;
    letter-spacing: 4px;
    color: var(--paper);
    -webkit-text-stroke: 1.5px var(--ink);
    text-shadow: 5px 3px 0 var(--gold-deep);
  }
  .varietal {
    top: 962px;
    font-family: "Pinyon Script", cursive;
    font-weight: 400;
    font-size: 108px;
    line-height: 1.1;
    color: var(--ink);
  }
  .spec {
    top: 1146px;
    font-family: "Didact Gothic", sans-serif;
    font-size: 42px;
    line-height: 1;
    letter-spacing: 1px;
    color: var(--ink);
  }
  .spec--abv { left: 38px; }
  .spec--volume { right: 38px; }
</style>
</head>
<body>
  <main class="label">
    <svg class="shade" viewBox="0 0 1005 1200" aria-hidden="true">
      <polygon points="0,329 1005,874 1005,1200 0,1200" fill="var(--shade)"/>
    </svg>
    <div class="stripes" aria-hidden="true"></div>

    <svg class="glass" viewBox="0 0 227 451" role="img" aria-label="Black wine glass silhouette">
      <rect x="0" y="0" width="227" height="451" rx="18" fill="var(--ink)"/>
    </svg>

    <div class="vintage">2014</div>
    <h1 class="brand">ROGUE</h1>
    <div class="varietal">Zinfandel</div>

    <div class="spec spec--abv">14.5% Vol.</div>
    <div class="spec spec--volume">750 ml</div>
  </main>
</body>
</html>
```